Cedar Hollow responsive web design

We need a responsive, bootstrap compatible (but design only - PSD files) website design for a fly fishing shop and guide service.

Design should be very clean. Home Page design + interior page design please.

Possible Home Page Content:
Slide Show
Highlight Three Features: Guided Trips, Fly Shop, Missouri River
About

Thank you and good luck!

Shop

• This will be used on Bootstrap CMS so needs 12 column bootstrap measurements.

DESIGN ONLY NEEDED (clean PSD files), no programming required.
Need a Home Page layout and secondary page layout

Must show use of the following:
H1 - H5 font uses
link color
Dropdown for navigation bar
Button example
• No cutout images, this will be part of CMS and client needs to be able to update most content without knowing photoshop.

```html
<!DOCTYPE html>
<html lang="en">
<head>
<meta charset="utf-8">
<title>Cedar Hollow — Fly Shop &amp; Guided Trips</title>
<link href="https://fonts.googleapis.com/css2?family=Open+Sans:ital,wght@0,300;0,400;0,600;0,700;1,300;1,400&display=swap" rel="stylesheet">
<style>
:root{
  --sky:#7fcdf0;
  --accent:#0a7fc0;
  --caption-blue:#5bc3e8;
  --ink:#2a2a2a;
  --text:#444;
  --muted:#9a9a9a;
  --card:#efefef;
  --dark:#1a0b0e;
  --dark-line:#33242a;
  --footer-text:#a89a9c;
  --pink:#e8808e;
  --white:#fff;
}
*{margin:0;padding:0;box-sizing:border-box}
html,body{width:832px;height:1200px;overflow:hidden;background:var(--white)}
body{position:relative;font-family:"Open Sans",sans-serif;color:var(--text)}
.abs{position:absolute}
.top-rule{left:0;top:0;width:832px;height:2px;background:var(--sky)}
.brand{left:76px;top:30px;display:flex;align-items:center;gap:7px;font-size:17px;font-weight:700;color:var(--accent)}
.brand-mark{width:14px;height:14px;background:var(--accent)}
.nav a{position:absolute;top:36px;font-size:10px;color:var(--ink);text-decoration:none;transform:translateX(-50%);white-space:nowrap}
.nav .home{font-weight:600}
.nav-active{left:492px;top:2px;width:76px;height:81px;background:var(--dark)}
.nav .active{color:var(--white);font-weight:600}
.dropdown{left:492px;top:83px;width:175px;height:80px;background:rgba(26,11,14,.9)}
.dropdown li{list-style:none;height:20px;padding-left:8px;font-size:9px;line-height:20px;color:#b7a7a9;border-bottom:1px solid #2e1e22}
.hero{left:0;top:83px;width:832px;height:352px;background:linear-gradient(160deg,#2f4a1a 0%,#6c8a2c 35%,#a8b04a 60%,#5f7630 80%,#3a4a22 100%)}
.caption{left:76px;top:178px;width:286px;height:146px;background:rgba(0,0,0,.78);padding:10px 14px}
.caption h1{font-size:20px;font-weight:300;color:var(--caption-blue);line-height:23px}
.caption h1 strong{font-weight:600;display:block}
.caption p{margin-top:13px;font-size:8.5px;line-height:11px;color:var(--white)}
.btn{display:inline-block;margin-top:16px;padding:6px 10px;background:#e8e8e8;color:var(--ink);font-size:10.5px;font-weight:600;border-radius:2px}
.section-title{left:0;top:486px;width:832px;text-align:center;font-size:21px;font-weight:300;color:var(--ink)}
.card{top:535px;width:221px;height:259px;background:var(--card)}
.card .photo{height:112px}
.card h3{margin-top:12px;text-align:center;font-size:14px;font-weight:300;color:var(--ink)}
.card p{margin:14px 11px 0;font-size:8.8px;line-height:14px;font-weight:300;color:var(--ink)}
.tab-head{height:18px;border-bottom:1px solid var(--accent)}
.tab-head span{display:inline-block;height:18px;padding:0 12px;background:var(--accent);color:var(--white);font-size:11px;line-height:18px}
.about{left:76px;top:825px;width:348px}
.about .photo{position:absolute;left:1px;top:27px;width:117px;height:80px;background:linear-gradient(135deg,#8a7a5a,#5b5a4a 50%,#9a8e70)}
.about p{margin:10px 0 0 125px;font-size:8.8px;line-height:14px;font-weight:300;color:var(--ink)}
.about a{display:block;margin:3px 0 0 125px;font-size:8.5px;color:var(--ink);text-decoration:underline}
.testimonial{left:484px;top:825px;width:272px}
.quote-box{margin-top:15px;height:102px;background:#f5f5f5;position:relative}
.quote-box svg{position:absolute;left:8px;top:10px}
.quote-box p{position:absolute;left:49px;top:8px;right:4px;font-size:8.8px;line-height:14px;font-style:italic;font-weight:300;color:#a0a0a0}
.author{position:absolute;right:0;top:143px;display:flex;gap:8px;align-items:center}
.avatar{width:26px;height:26px;background:linear-gradient(#9a9a9a,#5a5a5a)}
.author b{display:block;font-weight:400;font-size:11px;color:var(--pink)}
.author small{display:block;font-size:9px;color:#666;font-weight:600;white-space:nowrap}
.footer{left:0;top:1017px;width:832px;height:183px;background:var(--dark)}
.col{top:20px;font-size:9.5px;line-height:14px;font-weight:300;color:var(--footer-text)}
.col h4{font-size:10.5px;font-weight:400;color:var(--white);padding-bottom:9px;border-bottom:1px solid var(--dark-line);margin-bottom:18px}
.socials{display:flex;gap:5px;margin-top:6px}
.socials span{width:16px;height:16px;background:var(--accent);border-radius:2px}
.subscribe-form{display:flex;margin-top:9px}
.subscribe-form .field{width:115px;height:25px;background:var(--white);color:#aaa;padding-left:7px;line-height:25px;font-size:9.5px}
.subscribe-form .ok{width:34px;height:25px;border:1px solid #ddd;color:var(--white);text-align:center;line-height:23px;font-size:11px}
.footer-rule{left:88px;top:151px;width:668px;height:1px;background:var(--dark-line)}
.copyright{left:0;top:162px;width:832px;text-align:center;font-size:9px;color:#d8cccc}
</style>
</head>
<body>
<div class="abs top-rule"></div>

<header>
  <div class="abs brand"><span class="brand-mark"></span>Cedar Hollow</div>
  <div class="abs nav-active"></div>
  <nav class="nav">
    <svg class="abs" style="left:378px;top:22px" width="12" height="11" viewBox="0 0 12 11"><path d="M6 0L0 5.5h1.6V11h3.2V7.5h2.4V11h3.2V5.5H12z" fill="#2a2a2a"/></svg>
    <a class="home" style="left:384px">HOME</a>
    <a style="left:448px">ABOUT US</a>
    <a class="active" style="left:530px">GUIDED TRIPS</a>
    <a style="left:610px">FLY SHOP</a>
    <a style="left:708px">CREEKSIDE FLOATS</a>
  </nav>
</header>

<div class="abs hero" role="img" aria-label="Angler in waders casting a fly rod in a sunlit forest river"></div>
<ul class="abs dropdown">
  <li>Lorem Lipsum</li><li>Lorem Lipsum</li><li>Lorem Lipsum</li><li>Lorem Lipsum</li>
</ul>
<div class="abs caption">
  <h1>Then one tell better<strong>Fishing Stories</strong></h1>
  <p>It is a long established fact that a reader will be distracted by the readable content of a page when looking at its layout.</p>
  <span class="btn">READ MORE</span>
</div>

<h2 class="abs section-title">OUR SERVICES</h2>

<article class="abs card" style="left:76px">
  <div class="photo" role="img" aria-label="Group paddling a canoe on a forest lake" style="background:linear-gradient(#7d94b0,#3e5a35 35%,#3a4a70 60%,#2a3550)"></div>
  <h3>Guided Trips</h3>
  <p>It is a long established fact that a reader will be distracted by the readable content of a page when looking at its layout. The point of using Lorem Ipsum is that it has a more-or-less normal distribu-tion of letters, as opposed to using 'Content here, content here', making it look like readable English.</p>
</article>
<article class="abs card" style="left:306px">
  <div class="photo" role="img" aria-label="Fly shop storefront with a drift boat parked outside" style="background:linear-gradient(#9aa3aa,#c8c8c0 45%,#8a8070 70%,#6a6a66)"></div>
  <h3>Fly Shop</h3>
  <p>It is a long established fact that a reader will be distracted by the readable content of a page when looking at its layout. The point of using Lorem Ipsum is that it has a more-or-less normal distribu-tion of letters, as opposed to using 'Content here, content here', making it look like readable English.</p>
</article>
<article class="abs card" style="left:534px">
  <div class="photo" role="img" aria-label="River winding through a rocky canyon with pines" style="background:linear-gradient(#6a90c0,#9aa0a0 40%,#4a5a48 65%,#2e4a6a)"></div>
  <h3>Creekside Floats</h3>
  <p>It is a long established fact that a reader will be distracted by the readable content of a page when looking at its layout. The point of using Lorem Ipsum is that it has a more-or-less normal distribu-tion of letters, as opposed to using 'Content here, content here', making it look like readable English.</p>
</article>

<section class="abs about">
  <div class="tab-head"><span>ABOUT US</span></div>
  <div class="photo" role="img" aria-label="Two anglers in sunglasses on a boat"></div>
  <p>It is a long established fact that a reader will be distracted by the readable content of a page when looking at its layout. The point of using Lorem Ipsum is that it has a more-or-less normal distribution of letters, as opposed to using 'Content here, content here', making it look like readable English. Many desktop publishing packages and</p>
  <a>READ MORE</a>
</section>

<section class="abs testimonial" style="height:180px">
  <div class="tab-head"><span>OUR CLIENT SAY</span></div>
  <div class="quote-box">
    <svg width="38" height="28" viewBox="0 0 38 28"><path d="M0 28V14C0 6 4 1 12 0v5c-4 1-6 4-6 8h6v15zM20 28V14c0-8 4-13 12-14v5c-4 1-6 4-6 8h6v15z" fill="#dcdcdc"/></svg>
    <p>It is a long established fact that a reader will be dis-tracted by the readable content of a page when looking at its layout. The point of using Lorem Ipsum is that it has a more-or-less normal distribution of letters, as opposed to using 'Content here, content here', making it look like readable English. Many</p>
  </div>
  <div class="author">
    <div class="avatar" role="img" aria-label="Client portrait"></div>
    <div><b>SAM PORTER</b><small>Manager, Orchard Co</small></div>
  </div>
</section>

<footer class="abs footer">
  <div class="abs col" style="left:88px;width:205px">
    <h4>CONTACT US</h4>
    Pine Ridge, MT 59001<br>214 Alder Lane<br>phone: +1 406 555 0182<br>Fax: +1 406 555 0190<br>Email: hello@cedarhollow.example
  </div>
  <div class="abs col" style="left:298px;width:162px">
    <h4>GO SOCIAL</h4>
    Stay in touch with us:
    <div class="socials"><span></span><span></span><span></span><span></span><span></span><span></span></div>
  </div>
  <div class="abs col" style="left:568px;width:188px">
    <h4>SUBSCRIBE</h4>
    Enter your e-mail below to subscribe to our free newsletter.<br>We promise not to bother you often!
    <div class="subscribe-form"><div class="field">Enter Email</div><div class="ok">OK</div></div>
  </div>
  <div class="abs footer-rule"></div>
  <div class="abs copyright">© Cedar Hollow 2014. Privacy Policy | Terms of Service</div>
</footer>
</body>
</html>
```